Software as a Service to manage Home Care Management

We need a web site designed for Home Care Management Software as a Service product, that facilitates Home Care organizations to manage and schedule carers to visit client homes. We want a modern look and feel using our existing logo.

Target Market(s)

Home Care Management organizations. Product is similar to: https://kelvantro.co/

Coding

Coded - Design and coding required

Number of Pages Required

3 page

```html
<!DOCTYPE html>
<html lang="en">
<head>
<meta charset="utf-8">
<title>Tendwell – Home Care Management</title>
<link href="https://fonts.googleapis.com/css2?family=Jost:wght@400;500;600&family=Marcellus+SC&display=swap" rel="stylesheet">
<style>
:root{
  --pink:#f2457f;
  --pink-deep:#e3155c;
  --ink:#1f1f21;
  --text:#333;
  --muted:#555;
  --dark:#46464a;
  --darker:#222224;
  --white:#fff;
  --line:#e6e6e6;
}
*{box-sizing:border-box;margin:0;padding:0}
html,body{width:1200px;height:4501px;overflow:hidden}
body{position:relative;font-family:"Jost",sans-serif;color:var(--text);background:var(--white)}
.abs{position:absolute}
a{color:inherit;text-decoration:none}

/* header */
.site-header{position:absolute;left:0;top:0;width:1200px;height:90px;background:var(--white);z-index:5}
.brand{position:absolute;display:flex;align-items:center;gap:9px;font-family:"Jost",sans-serif;font-weight:500;color:var(--ink);letter-spacing:.5px}
.brand-dot{width:26px;height:26px;border-radius:50%;background:var(--pink)}
.site-header .brand{left:178px;top:26px;font-size:26px}
.main-nav{position:absolute;left:518px;top:38px;display:flex;gap:22px;font-size:16px;color:var(--ink)}
.btn{display:inline-flex;align-items:center;justify-content:center;border-radius:30px;font-family:"Jost",sans-serif;font-weight:600;text-transform:uppercase}
.btn-login{position:absolute;left:934px;top:28px;width:92px;height:44px;background:var(--pink);color:var(--white);font-size:14px}

/* hero */
.hero-photo{position:absolute;left:0;top:90px;width:1200px;height:740px;background:linear-gradient(120deg,#3d5a32 0%,#6b8a55 35%,#b6a99a 60%,#8a4b3c 100%)}
.hero-title{position:absolute;left:175px;top:295px;width:560px;font-family:"Marcellus SC",serif;font-size:42px;line-height:58px;color:var(--white)}
.btn-hero{position:absolute;left:175px;top:448px;width:222px;height:56px;background:var(--pink);color:var(--white);font-size:20px;text-transform:uppercase;font-weight:500}
.phone{position:absolute;background:#111;border-radius:34px;padding:10px}
.phone-screen{width:100%;height:100%;background:var(--white);border-radius:26px;overflow:hidden;position:relative}
.phone-hero{left:846px;top:245px;width:246px;height:502px}
.phone-hero .brand{left:32px;top:68px;font-size:20px}
.phone-hero .brand-dot{width:20px;height:20px}
.screen-photo{position:absolute;background:linear-gradient(135deg,#7a5a3e 0%,#5d8a66 55%,#9fb4a0 100%)}
.tabbar{position:absolute;left:0;bottom:0;width:100%;height:44px;display:flex;justify-content:space-around;align-items:center}
.tabbar span{width:14px;height:14px;border-radius:50%;background:#222}

/* section heads */
.section-mark{position:absolute;left:594px;width:12px;height:12px;border-radius:50%;background:var(--pink)}
.section-title{position:absolute;left:0;width:1200px;text-align:center;font-size:38px;font-weight:500;color:var(--ink);text-transform:uppercase}
.section-lead{position:absolute;left:200px;width:800px;text-align:center;font-size:12.5px;line-height:22px;color:var(--ink)}

/* cards */
.card{position:absolute;background:var(--white);border-radius:6px;box-shadow:0 2px 12px rgba(0,0,0,.12);text-align:center}
.card.is-active{background:linear-gradient(180deg,var(--pink),var(--pink-deep));color:var(--white)}
.card-icon{display:block;margin:20px auto 0}
.card-title{font-size:16px;font-weight:500;text-transform:uppercase;color:var(--ink)}
.card-text{font-size:12.5px;line-height:22px;color:var(--muted);padding:0 26px}
.card.is-active .card-title,.card.is-active .card-text{color:var(--white)}
.btn-card{width:96px;height:40px;background:#3a3a3c;color:var(--white);font-size:12px;font-weight:600;margin-top:14px}
.card.is-active .btn-card{background:var(--white);color:var(--pink)}
.card-photo{height:190px;border-radius:6px 6px 0 0;margin:0}

/* optimised */
.optimised-bg{position:absolute;left:0;top:1385px;width:1200px;height:822px}
.optimised-title{position:absolute;left:612px;top:1752px;font-size:38px;line-height:44px;color:var(--white);font-weight:400}
.feature-list{position:absolute;left:612px;top:1866px;list-style:none;color:var(--white);font-size:13.5px}
.feature-list li{display:flex;align-items:center;gap:18px;height:30px}
.btn-outline{position:absolute;height:40px;border:1.5px solid var(--white);color:var(--white);font-size:12.5px;font-weight:500}
.btn-solid-white{position:absolute;height:40px;background:var(--white);color:var(--pink);font-size:12.5px;font-weight:600}

/* numbers */
.numbers-bg{position:absolute;left:0;top:2900px;width:1200px;height:692px}
.stat{position:absolute;top:3248px;width:234px;height:234px;border-radius:50%;border:3px solid var(--white);overflow:hidden;text-align:center;color:var(--white)}
.stat-value{margin-top:42px;font-size:58px;font-weight:600;line-height:70px}
.stat-label{font-size:18px;line-height:26px;text-transform:uppercase;margin-top:6px}
.stat.is-active .stat-fill{position:absolute;left:0;top:128px;width:100%;height:110px;background:var(--pink)}
.stat.is-active .stat-label{position:relative;margin-top:12px}

/* contact */
.contact-title{position:absolute;left:497px;top:3690px;font-size:34px;font-weight:500;color:var(--ink);text-transform:uppercase}
.field{position:absolute;background:var(--white);border:1px solid var(--line);border-radius:28px;box-shadow:0 2px 8px rgba(0,0,0,.08);font-size:13px;color:var(--ink);padding:18px 18px}
.btn-send{position:absolute;left:497px;top:4044px;width:134px;height:60px;background:var(--pink);color:var(--white);font-size:17px;font-weight:500}
.phone-contact{left:200px;top:3690px;width:212px;height:430px;background:#1a1a1a;border:3px solid #cfcfcf}

/* footer */
.footer-bg{position:absolute;left:0;top:4150px;width:1200px;height:351px}
.footer-nav{position:absolute;left:630px;top:4336px;display:flex;gap:22px;font-size:15px;color:var(--white)}
.footer-rule{position:absolute;left:555px;top:4390px;width:472px;height:1px;background:#8a8a8a}
.footer .brand{left:176px;top:4402px;font-size:28px;color:var(--white)}
.copyright{position:absolute;left:654px;top:4434px;font-size:15px;color:var(--white)}
</style>
</head>
<body>

<header class="site-header">
  <div class="brand"><span class="brand-dot"></span>Tendwell</div>
  <nav class="main-nav">
    <a href="#">Home</a><a href="#">Product</a><a href="#">Pricing</a><a href="#">Blog</a><a href="#">FAQ</a><a href="#">Contact Us</a>
  </nav>
  <a class="btn btn-login" href="#">Log in</a>
</header>

<!-- hero -->
<section class="hero">
  <div class="hero-photo" role="img" aria-label="Carer helping a smiling elderly woman in a wheelchair outside a brick house"></div>
  <svg class="abs" style="left:0;top:500px" width="1200" height="340" viewBox="0 0 1200 340">
    <path d="M0 340 L0 320 C60 330 110 300 170 270 C300 200 420 300 600 250 C760 205 800 130 960 90 C1060 65 1130 60 1200 40 L1200 340 Z" fill="#fff"/>
  </svg>
  <h1 class="hero-title">Care Software for the Heroes of Homecare</h1>
  <a class="btn btn-hero" href="#">See how it works</a>
  <div class="phone phone-hero">
    <div class="phone-screen">
      <div class="brand"><span class="brand-dot"></span>Tendwell</div>
      <div class="screen-photo" style="left:14px;top:130px;width:198px;height:284px" role="img" aria-label="Carer with an elderly woman in a wheelchair"></div>
      <div class="tabbar"><span></span><span></span><span></span><span></span><span></span></div>
    </div>
  </div>
</section>

<!-- why -->
<section class="why">
  <span class="section-mark" style="top:872px"></span>
  <h2 class="section-title" style="top:906px">Why Tendwell</h2>
  <p class="section-lead" style="top:974px">Nemo enim ipsam voluptatem quia voluptas sit aspernatur aut odit aut fugit, sed quia consequuntur magni dolores eos qui ratione voluptatem</p>

  <div class="card" style="left:172px;top:1066px;width:264px;height:268px">
    <svg class="card-icon" width="60" height="70" viewBox="0 0 60 70" fill="none" stroke="#333" stroke-width="2"><rect x="20" y="4" width="20" height="12" rx="3"/><path d="M28 10h4M30 8v4"/><circle cx="30" cy="32" r="14"/><path d="M16 32c-2 14 -6 20 -10 26M44 32c2 14 6 20 10 26M18 66c4-8 20-8 24 0"/></svg>
    <p class="card-title" style="margin-top:14px">Home Care Software</p>
    <p class="card-text" style="margin-top:8px">Sed ut perspiciatis unde omnis iste natus error sit voluptatem</p>
    <a class="btn btn-card" href="#">Read more</a>
  </div>
  <div class="card is-active" style="left:468px;top:1066px;width:264px;height:268px">
    <svg class="card-icon" width="60" height="70" viewBox="0 0 60 70" fill="none" stroke="#fff" stroke-width="2"><circle cx="30" cy="18" r="8"/><path d="M18 40c0-8 24-8 24 0"/><path d="M6 30v20l14 14M54 30v20l-14 14M12 44l10 8M48 44l-10 8"/></svg>
    <p class="card-title" style="margin-top:14px">Easy to Set</p>
    <p class="card-text" style="margin-top:8px">Sed ut perspiciatis unde omnis iste natus error sit voluptatem</p>
    <a class="btn btn-card" href="#">Read more</a>
  </div>
  <div class="card" style="left:763px;top:1066px;width:264px;height:268px">
    <svg class="card-icon" width="64" height="70" viewBox="0 0 64 70" fill="none" stroke="#333" stroke-width="2"><rect x="4" y="8" width="56" height="38" rx="3"/><path d="M16 38v-8M22 38v-12M28 38v-16M34 38v-20"/><circle cx="48" cy="20" r="6"/><path d="M32 46v10M18 62h28"/></svg>
    <p class="card-title" style="margin-top:14px">Reporting Suite</p>
    <p class="card-text" style="margin-top:8px">Sed ut perspiciatis unde omnis iste natus error sit voluptatem</p>
    <a class="btn btn-card" href="#">Read more</a>
  </div>
</section>

<!-- optimised -->
<section class="optimised">
  <svg class="optimised-bg" viewBox="0 0 1200 822" preserveAspectRatio="none" role="img" aria-label="Carer with an elderly client at home under a pink tint">
    <defs><linearGradient id="pinkFill" x1="0" y1="0" x2="1" y2="1"><stop offset="0" stop-color="#f55a8e"/><stop offset="1" stop-color="#ee3f7a"/></linearGradient></defs>
    <path d="M0 40 C60 0 110 60 200 100 C320 150 420 70 560 80 C700 90 780 180 900 170 C1020 160 1100 150 1200 190 L1200 822 L0 822 Z" fill="url(#pinkFill)"/>
  </svg>
  <div class="phone" style="left:258px;top:1648px;width:184px;height:370px;border:3px solid #ddd">
    <div class="phone-screen">
      <div class="brand" style="left:22px;top:58px;font-size:18px"><span class="brand-dot" style="width:16px;height:16px"></span>Tendwell</div>
      <p class="abs" style="left:0;top:136px;width:100%;text-align:center;color:var(--pink);font-size:20px;text-transform:uppercase">Nurses</p>
      <div class="abs" style="left:22px;top:182px;width:58px;height:58px;border-radius:50%;background:#c79a7b" role="img" aria-label="Nurse profile photo"></div>
      <div class="abs" style="left:94px;top:182px;width:58px;height:58px;border-radius:50%;background:#b88763" role="img" aria-label="Nurse profile photo"></div>
    </div>
  </div>
  <span class="abs" style="left:614px;top:1714px;width:14px;height:14px;border-radius:50%;background:var(--white)"></span>
  <h2 class="optimised-title">OPTIMISED HOME CARE<br>SOFTWARE</h2>
  <ul class="feature-list">
    <li><svg width="18" height="14" viewBox="0 0 18 14" fill="none" stroke="#fff" stroke-width="2"><path d="M2 7l5 5 9-10"/></svg>All-in-one home care software</li>
    <li><svg width="18" height="14" viewBox="0 0 18 14" fill="none" stroke="#fff" stroke-width="2"><path d="M2 7l5 5 9-10"/></svg>Create staff rotas with automated scheduling tools</li>
    <li><svg width="18" height="14" viewBox="0 0 18 14" fill="none" stroke="#fff" stroke-width="2"><path d="M2 7l5 5 9-10"/></svg>Tailored care plans &amp; risk assessments for your clients</li>
    <li><svg width="18" height="14" viewBox="0 0 18 14" fill="none" stroke="#fff" stroke-width="2"><path d="M2 7l5 5 9-10"/></svg>Check in/out from a client visit using the app</li>
    <li><svg width="18" height="14" viewBox="0 0 18 14" fill="none" stroke="#fff" stroke-width="2"><path d="M2 7l5 5 9-10"/></svg>Reporting suite for payroll, invoices, inspections &amp; more!</li>
    <li><svg width="18" height="14" viewBox="0 0 18 14" fill="none" stroke="#fff" stroke-width="2"><path d="M2 7l5 5 9-10"/></svg>Easy to set up and use. Get started today!</li>
  </ul>
  <a class="btn btn-solid-white" style="left:651px;top:2076px;width:92px" href="#">Read more</a>
  <a class="btn btn-outline" style="left:756px;top:2076px;width:152px" href="#">Book a free demo</a>
</section>

<!-- who we serve -->
<section class="serve">
  <span class="section-mark" style="top:2290px"></span>
  <h2 class="section-title" style="top:2322px">Who We Serve For</h2>

  <div class="card" style="left:172px;top:2426px;width:250px;height:384px">
    <div class="card-photo" style="margin:10px 0 0 -16px;width:256px;background:linear-gradient(135deg,#d9d2c6,#5a5c64 60%,#9c9387)" role="img" aria-label="Manager working on paperwork at a desk"></div>
    <p class="card-title" style="margin-top:22px">For Managers</p>
    <p class="card-text" style="margin-top:8px">Sed ut perspiciatis unde omnis iste natus error sit voluptatem</p>
    <a class="btn btn-card" href="#">Read more</a>
  </div>
  <div class="card is-active" style="left:484px;top:2420px;width:248px;height:390px">
    <div class="card-photo" style="margin:10px 0 0 -16px;width:256px;background:linear-gradient(135deg,#e9e4dd,#7c8590 50%,#2d3a55)" role="img" aria-label="Carer supporting an elderly man in his armchair"></div>
    <p class="card-title" style="margin-top:22px">For Carers</p>
    <p class="card-text" style="margin-top:8px">Sed ut perspiciatis unde omnis iste natus error sit voluptatem</p>
    <a class="btn btn-card" href="#">Read more</a>
  </div>
  <div class="card" style="left:778px;top:2426px;width:250px;height:384px">
    <div class="card-photo" style="margin:10px 0 0 -16px;width:256px;background:linear-gradient(135deg,#c8ccd2,#4e5663 55%,#8a96a6)" role="img" aria-label="Family members meeting around a table"></div>
    <p class="card-title" style="margin-top:22px">For Clients and Families</p>
    <p class="card-text" style="margin-top:8px">Sed ut perspiciatis unde omnis iste natus error sit voluptatem</p>
    <a class="btn btn-card" href="#">Read more</a>
  </div>
</section>

<!-- numbers -->
<section class="numbers">
  <svg class="numbers-bg" viewBox="0 0 1200 692" preserveAspectRatio="none" role="img" aria-label="Carer with an elderly client under a dark grey tint">
    <path d="M0 100 C120 40 260 30 400 70 C560 115 700 70 860 40 C990 15 1100 0 1200 10 L1200 692 L0 692 Z" fill="#b3b3b5"/>
    <path d="M0 130 C140 100 260 70 420 110 C560 145 680 120 840 80 C980 45 1100 30 1200 40 L1200 692 L0 692 Z" fill="var(--dark)"/>
  </svg>
  <span class="abs" style="left:594px;top:3104px;width:12px;height:12px;border-radius:50%;background:var(--white)"></span>
  <h2 class="section-title" style="top:3138px;color:var(--white)">Success in Numbers</h2>
  <div class="stat" style="left:174px"><p class="stat-value">92%</p><p class="stat-label">Customer Support<br>Happiness</p></div>
  <div class="stat is-active" style="left:484px"><span class="stat-fill"></span><p class="stat-value" style="position:relative">10M</p><p class="stat-label">Total Care Hours<br>Managed</p></div>
  <div class="stat" style="left:793px"><p class="stat-value">16K</p><p class="stat-label">Active Tendwell<br>Users</p></div>
</section>

<!-- contact -->
<section class="contact">
  <div class="phone phone-contact">
    <div class="phone-screen">
      <div class="brand" style="left:16px;top:108px;font-size:22px"><span class="brand-dot" style="width:18px;height:18px"></span>Tendwell</div>
      <div class="screen-photo" style="left:14px;top:168px;width:172px;height:204px;background:linear-gradient(135deg,#b7a79a,#4b5a7a 60%,#d9c7b6)" role="img" aria-label="Carer assisting a seated client"></div>
    </div>
  </div>
  <h2 class="contact-title">Want to Know More?</h2>
  <div class="field" style="left:497px;top:3766px;width:262px;height:56px">Name*</div>
  <div class="field" style="left:765px;top:3766px;width:262px;height:56px">Company Name*</div>
  <div class="field" style="left:497px;top:3841px;width:262px;height:56px">Phone Number*</div>
  <div class="field" style="left:765px;top:3841px;width:262px;height:56px">Email*</div>
  <div class="field" style="left:497px;top:3916px;width:530px;height:108px">Message</div>
  <a class="btn btn-send" href="#">Send now</a>
</section>

<!-- footer -->
<footer class="footer">
  <svg class="footer-bg" viewBox="0 0 1200 351" preserveAspectRatio="none">
    <path d="M0 220 C120 120 220 130 360 160 C520 195 640 200 800 150 C960 100 1080 60 1200 0 L1200 351 L0 351 Z" fill="var(--darker)"/>
  </svg>
  <nav class="footer-nav"><a href="#">Home</a><a href="#">Product</a><a href="#">Pricing</a><a href="#">Blog</a><a href="#">FAQ</a><a href="#">Contact Us</a></nav>
  <span class="footer-rule"></span>
  <div class="brand"><span class="brand-dot"></span>Tendwell</div>
  <p class="copyright">Copyrights @ 2020 Tendwell. All Rights Reserved.</p>
</footer>

</body>
</html>
```